Business Cards, Letterheads, Envelopes

A company's new identity to be reflected on its stationery items

Target Market(s)

Large Corporate Companies & Enterprises

Font styles to use
Sans Serif

Colors
0555a3
3176b5
85abd2
85cae6
33a6d7
0293ce

```html
<!DOCTYPE html>
<html lang="en">
<head>
<meta charset="utf-8">
<title>Northvale Systems – Envelope Set</title>
<link rel="stylesheet" href="https://fonts.googleapis.com/css2?family=Open+Sans:wght@400;600&family=Exo+2:wght@600&display=swap">
<style>
  :root {
    --navy: #0555a3;
    --mid-blue: #3176b5;
    --soft-blue: #85abd2;
    --sky: #85cae6;
    --cyan: #33a6d7;
    --bright: #0293ce;
    --paper: #f7f8f9;
    --paper-shade: #eceef0;
    --text-grey: #5b6168;
    --backdrop: #eef2f6;
  }
  * { margin: 0; padding: 0; box-sizing: border-box; }
  html, body { width: 1200px; height: 950px; overflow: hidden; background: var(--backdrop); }
  .canvas { position: relative; width: 1200px; height: 950px; font-family: "Open Sans", sans-serif; }

  /* Envelope front */
  .envelope-front {
    position: absolute; left: 180px; top: 30px; width: 840px; height: 400px;
    background: var(--paper); box-shadow: 0 6px 18px rgba(5,85,163,.15);
  }
  .brand { position: absolute; left: 50px; top: 58px; display: flex; align-items: center; gap: 14px; }
  .brand-dot { width: 44px; height: 44px; border-radius: 50%; background: var(--mid-blue); flex: none; }
  .brand-text { display: flex; flex-direction: column; }
  .brand-name {
    font-family: "Exo 2", sans-serif; font-weight: 600; font-size: 22px; line-height: 1.05;
    color: var(--mid-blue); text-transform: uppercase; letter-spacing: .5px; white-space: nowrap;
  }
  .brand-tagline {
    margin-top: 6px; padding-top: 4px; border-top: 1px solid var(--soft-blue);
    font-size: 8.5px; letter-spacing: 3px; text-transform: uppercase; color: var(--text-grey);
  }
  .contact-line {
    position: absolute; left: 20px; bottom: 26px; width: 600px; display: flex; gap: 12px;
    font-size: 9.5px; color: var(--text-grey); align-items: center; white-space: nowrap;
  }
  .contact-item { display: flex; align-items: center; gap: 4px; }
  .contact-item svg { width: 10px; height: 10px; flex: none; }
  .footer-band { position: absolute; left: 0; bottom: 0; width: 840px; height: 44px; }
  .web-address {
    position: absolute; right: 20px; bottom: 15px; font-size: 13px; font-weight: 600; color: #fff;
    white-space: nowrap;
  }

  /* Envelope back */
  .envelope-back { position: absolute; left: 180px; top: 470px; width: 840px; height: 470px; }
  .envelope-back svg.shape { position: absolute; inset: 0; }
  .back-mark {
    position: absolute; right: 150px; bottom: 120px; display: flex; align-items: center; gap: 10px;
  }
  .back-mark .brand-dot { width: 34px; height: 34px; }
  .back-mark .brand-name { font-size: 16px; }
</style>
</head>
<body>
<main class="canvas">

  <section class="envelope-front" aria-label="Envelope front">
    <div class="brand">
      <span class="brand-dot"></span>
      <div class="brand-text">
        <span class="brand-name">Northvale Systems</span>
        <span class="brand-name">Private Limited</span>
        <span class="brand-tagline">Powered by Innovation</span>
      </div>
    </div>

    <svg class="footer-band" viewBox="0 0 840 44" preserveAspectRatio="none" aria-hidden="true">
      <defs>
        <linearGradient id="band" x1="0" y1="0" x2="0" y2="1">
          <stop offset="0" stop-color="#3176b5"/>
          <stop offset="1" stop-color="#0555a3"/>
        </linearGradient>
      </defs>
      <rect x="0" y="38" width="840" height="6" fill="url(#band)"/>
      <polygon points="340,38 350,31 500,31 490,38" fill="#3176b5"/>
      <polygon points="640,38 660,0 840,0 840,44 640,44" fill="url(#band)"/>
      <rect x="0" y="35" width="640" height="1" fill="#85abd2"/>
    </svg>

    <div class="contact-line">
      <span class="contact-item">
        <svg viewBox="0 0 12 12"><circle cx="6" cy="6" r="5.5" fill="#3176b5"/><circle cx="6" cy="5" r="1.8" fill="#fff"/></svg>
        #42-B, Lakeview Business Park, Pune - 411014 Maharashtra (INDIA)
      </span>
      <span class="contact-item">
        <svg viewBox="0 0 12 12"><rect width="12" height="12" rx="2" fill="#3176b5"/><path d="M3.5 3h2l.5 2-1 .8a5 5 0 0 0 2 2l.8-1 2 .5v2a1 1 0 0 1-1 1A6.5 6.5 0 0 1 2.5 4a1 1 0 0 1 1-1z" fill="#fff"/></svg>
        +91 800 555 0199
      </span>
      <span class="contact-item">
        <svg viewBox="0 0 12 12"><rect width="12" height="12" rx="2" fill="#3176b5"/><rect x="2.5" y="3.5" width="7" height="5" fill="none" stroke="#fff"/><path d="M2.5 3.5 6 6.5l3.5-3" fill="none" stroke="#fff"/></svg>
        info@northvalesys.com
      </span>
    </div>

    <span class="web-address">www.northvalesys.com</span>
  </section>

  <section class="envelope-back" aria-label="Envelope back">
    <svg class="shape" viewBox="0 0 840 470">
      <defs>
        <linearGradient id="flapTone" x1="0" y1="0" x2="0" y2="1">
          <stop offset="0" stop-color="#3176b5"/>
          <stop offset="1" stop-color="#0555a3"/>
        </linearGradient>
      </defs>
      <path d="M0 90 L40 0 H800 L840 90 Z" fill="url(#flapTone)" role="img" aria-label="Inner flap printed with a blue interlocking geometric pattern"/>
      <rect x="0" y="90" width="840" height="380" fill="#f7f8f9"/>
      <path d="M0 90 L360 300 Q420 330 480 300 L840 90" fill="none" stroke="#eceef0" stroke-width="2"/>
      <path d="M0 470 L330 290 M840 470 L510 290" stroke="#eceef0" stroke-width="2"/>
    </svg>
    <div class="back-mark">
      <span class="brand-dot"></span>
      <span class="brand-name">Northvale Systems</span>
    </div>
  </section>

</main>
</body>
</html>
```